Cascade Rhythm Guild Business Cards

The Cascade Rhythm Guild is a non-profit organization that supports, promotes, and manages music events in the Pacific Northwest. Our mission is to keep the blues alive. We do this by partnering with local venues, schools, and national acts to bring some of the best blues music to our members. As newly elected Executive Board Members we would like to have new business cards designed. I have included a copy of our logo.

```html
<!DOCTYPE html>
<html lang="en">
<head>
<meta charset="utf-8">
<title>Cascade Rhythm Guild Business Cards</title>
<link href="https://fonts.googleapis.com/css2?family=Montserrat:wght@400;700&display=swap" rel="stylesheet">
<style>
  :root {
    --bg: #d3d3d3;
    --card: #f2f1ee;
    --edge: #5b9bd8;
    --blue: #4f9be0;
    --grey: #7a7a7a;
    --rule: #cfcdc8;
    --accent: #e8662a;
    --sun: #f6ef8f;
  }
  * { margin: 0; padding: 0; box-sizing: border-box; }
  html, body { width: 1200px; height: 1051px; overflow: hidden; }
  body {
    background: var(--bg);
    font-family: "Montserrat", sans-serif;
    position: relative;
  }
  .card {
    position: absolute;
    left: 330px;
    width: 540px;
    height: 309px;
    background: var(--card);
    border-bottom: 5px solid var(--edge);
    box-shadow: 0 14px 30px rgba(0,0,0,0.18);
  }
  .card--front { top: 150px; }
  .card--back { top: 590px; }

  .brand {
    display: flex;
    align-items: center;
    gap: 12px;
  }
  .brand__dot {
    width: 46px; height: 46px;
    border-radius: 50%;
    background: var(--sun);
    flex: none;
  }
  .brand__name {
    font-weight: 700;
    color: var(--blue);
    font-size: 19px;
    line-height: 1.15;
  }

  .card--front .brand {
    position: absolute;
    left: 34px; top: 0; bottom: 0;
    width: 205px;
  }
  .divider {
    position: absolute;
    left: 258px; top: 58px;
    width: 2px; height: 170px;
    background: var(--rule);
  }
  .contact {
    position: absolute;
    left: 282px; top: 58px;
    color: var(--grey);
  }
  .contact__name {
    color: var(--blue);
    font-weight: 700;
    font-size: 17px;
    letter-spacing: 0.5px;
  }
  .contact__role { font-size: 12px; margin-top: 2px; }
  .contact__address { font-size: 12px; margin-top: 18px; line-height: 1.45; }
  .contact__list { list-style: none; margin-top: 16px; font-size: 12px; line-height: 1.6; }
  .contact__list li { display: flex; align-items: center; gap: 7px; }
  .contact__list svg { width: 11px; height: 11px; flex: none; }

  .card--back .brand {
    position: absolute;
    inset: 0;
    justify-content: center;
  }
  .card--back .brand__dot { width: 64px; height: 64px; }
  .card--back .brand__name { font-size: 26px; }
</style>
</head>
<body>
  <section class="card card--front">
    <div class="brand">
      <span class="brand__dot"></span>
      <span class="brand__name">Cascade Rhythm Guild</span>
    </div>
    <div class="divider"></div>
    <div class="contact">
      <p class="contact__name">MARTIN CALDWELL</p>
      <p class="contact__role">President</p>
      <p class="contact__address">4180 Alder Ridge Way<br>Tacoma WA 98402</p>
      <ul class="contact__list">
        <li>
          <svg viewBox="0 0 12 12" aria-hidden="true"><path d="M3 1l2 2.5-1.2 1.3a6 6 0 0 0 3.4 3.4L8.5 7 11 9l-1.3 1.8C5.5 11 1 6.5 1.2 2.3z" fill="var(--accent)"/></svg>
          555-014-2287
        </li>
        <li>
          <svg viewBox="0 0 12 12" aria-hidden="true"><rect x="1" y="2.5" width="10" height="7" fill="var(--accent)"/><path d="M1 2.8l5 3.6 5-3.6" stroke="#fff" fill="none" stroke-width="1"/></svg>
          info@CascadeRhythm.org
        </li>
        <li>
          <svg viewBox="0 0 12 12" aria-hidden="true"><circle cx="6" cy="6" r="5" fill="var(--accent)"/><path d="M1 6h10M6 1c-2 2.5-2 7.5 0 10M6 1c2 2.5 2 7.5 0 10" stroke="#fff" fill="none" stroke-width="0.8"/></svg>
          www.CascadeRhythm.org
        </li>
      </ul>
    </div>
  </section>

  <section class="card card--back">
    <div class="brand">
      <span class="brand__dot"></span>
      <span class="brand__name">Cascade Rhythm Guild</span>
    </div>
  </section>
</body>
</html>
```